Business Card Design Project

Business Card
We are rebranding with a new logo
Industry/Entity Type
Business
Contact Information for Business Card
Dennis Marlow +61 427581962 dennis@qovo.com.au P.O. Box 872 Kelvindale QLD 4309
Requirements
Must have
- Logo

```html
<!DOCTYPE html>
<html lang="en">
<head>
<meta charset="utf-8">
<title>Qovo International – Business Card</title>
<link rel="stylesheet" href="https://fonts.googleapis.com/css2?family=Open+Sans:wght@400;600;700&display=swap">
<style>
  :root {
    --backdrop: #1e1e1e;
    --card: #f7f7f5;
    --brand-blue: #1f8fc4;
    --brand-blue-deep: #1778ad;
    --brand-orange: #e0622a;
    --brand-amber: #f0993a;
    --ink: #2f2f2f;
    --icon-glyph: #ffffff;
  }
  * { box-sizing: border-box; margin: 0; padding: 0; }
  html, body {
    width: 1200px;
    height: 800px;
    overflow: hidden;
    background: var(--backdrop);
    font-family: "Open Sans", Arial, sans-serif;
  }
  .business-card {
    position: absolute;
    left: 150px;
    top: 130px;
    width: 900px;
    height: 540px;
    background: var(--card);
    border-radius: 34px;
    overflow: hidden;
  }
  .brand-graphic {
    position: absolute;
    left: 400px;
    top: 0;
    width: 150px;
    height: 430px;
    border-radius: 0 0 75px 75px;
    background: linear-gradient(160deg, var(--brand-blue-deep) 0%, var(--brand-blue) 55%, var(--brand-amber) 100%);
    opacity: 0.9;
  }
  .holder {
    position: absolute;
    left: 80px;
    top: 205px;
  }
  .holder-name {
    font-size: 29px;
    font-weight: 700;
    letter-spacing: 1px;
    text-transform: uppercase;
    color: var(--brand-orange);
    margin-bottom: 20px;
    white-space: nowrap;
  }
  .contact-list { list-style: none; }
  .contact-item {
    display: flex;
    align-items: flex-start;
    gap: 14px;
    font-size: 21px;
    line-height: 29px;
    color: var(--ink);
    margin-bottom: 10px;
    white-space: nowrap;
  }
  .contact-icon {
    flex: 0 0 27px;
    width: 27px;
    height: 27px;
    margin-top: 1px;
  }
  .brand {
    position: absolute;
    left: 575px;
    top: 262px;
    display: flex;
    align-items: center;
    gap: 12px;
    white-space: nowrap;
  }
  .brand-dot {
    width: 24px;
    height: 24px;
    border-radius: 50%;
    background: var(--brand-blue);
  }
  .brand-name {
    font-size: 26px;
    font-weight: 600;
    color: var(--brand-blue);
    letter-spacing: 0.5px;
  }
</style>
</head>
<body>
  <main class="business-card">
    <div class="brand-graphic" role="img" aria-label="Large brand graphic in blue and orange tones"></div>

    <section class="holder">
      <h1 class="holder-name">Dennis Marlow</h1>
      <ul class="contact-list">
        <li class="contact-item">
          <svg class="contact-icon" viewBox="0 0 28 28" aria-hidden="true">
            <circle cx="14" cy="14" r="14" fill="var(--brand-blue)"/>
            <path d="M10 7.5c.6-.4 1.3-.2 1.6.4l1.2 2.4c.3.6.1 1.2-.4 1.6l-1 .7c.7 1.7 2 3.1 3.6 4l.8-.9c.4-.5 1.1-.6 1.6-.3l2.3 1.4c.6.3.8 1 .4 1.6l-.9 1.3c-.5.7-1.4 1-2.2.8-4.2-1.2-7.4-4.5-8.5-8.8-.2-.8.1-1.6.8-2.1z" fill="var(--icon-glyph)"/>
          </svg>
          <span>+61 427 581 962</span>
        </li>
        <li class="contact-item">
          <svg class="contact-icon" viewBox="0 0 28 28" aria-hidden="true">
            <circle cx="14" cy="14" r="14" fill="var(--brand-blue)"/>
            <rect x="7.5" y="9" width="13" height="10" rx="1.2" fill="var(--icon-glyph)"/>
            <path d="M8 9.8l6 4.6 6-4.6" fill="none" stroke="var(--brand-blue)" stroke-width="1.4"/>
          </svg>
          <span>dennis@qovo.com.au</span>
        </li>
        <li class="contact-item">
          <svg class="contact-icon" viewBox="0 0 28 28" aria-hidden="true">
            <circle cx="14" cy="14" r="14" fill="var(--brand-blue)"/>
            <path d="M14 6.5c-3 0-5.3 2.3-5.3 5.2 0 3.8 5.3 9.8 5.3 9.8s5.3-6 5.3-9.8c0-2.9-2.3-5.2-5.3-5.2z" fill="var(--icon-glyph)"/>
            <circle cx="14" cy="11.8" r="2" fill="var(--brand-blue)"/>
          </svg>
          <span>P.O. Box 872 Kelvindale<br>QLD 4309</span>
        </li>
      </ul>
    </section>

    <div class="brand">
      <span class="brand-dot" aria-hidden="true"></span>
      <span class="brand-name">Qovo International</span>
    </div>
  </main>
</body>
</html>
```